*** Einladungsdesign für Start-up Event gesucht ***
Zielgruppe
Für eine innovative Start-up Veranstaltung suchen wir ein stylishes, progressives Layout für die Einladungskarten. Die Veranstaltung heißt
#ThinkAheadNow
und soll als schlichter Schriftzug in die Einladungen eingearbeitet sein. Die exakte Schriftart hierfür etc. wird noch übermittelt. Im Gegensatz das restliche Design gerne futuristisch und modern gehalten sein. Dennoch insgesamt hochwertiger Gesamteindruck
Aufgabenstellung
Name: #ThinkAheadNow
Daten: 4 Seiten
Deckblatt.
linke Innenseite: kurzer Text/Grußwort:
YOUNG. CREATIVE. NIGHT.
Das Internet hat die Welt verändert und sich tief in unserer Gesellschaft verankert. Es ist die Chance unserer Generation diese Digitalisierung zu nutzen und die Welt von morgen weiterzuentwickeln
Freuen Sie sich auf eine inspirierende Nacht im Zeichen der „young leading minds of our time“. Ein Podium für Macher von heute und morgen.
FAST. FORWARD. FUTURE.
rechte Innenseite: Einladungstext
Wir freuen uns
_______________________________ (hier wird Name handschriftlich eingetragen)
zur exklusiven #ThinkAheadNow-Night
einladen zu dürfen.
Datum: 01. Februar 2015
Uhrzeit: ab 20:30 Uhr
Ort: xxxxxx, Anfahrt über xxxxxxx
r.s.v.p. bis zum 14. Januar 2014 unter xxxxxxx
Rückseite: Sponsoren & Partner der Veranstaltung
Stehen noch nicht fest, daher bitte einfach mit ca. 5 farbigen Logos (z.B. Vemko AG) arbeiten.
Farbwelt: Gerne an verschiedenen Grautönen, Schwarz und Rot orientieren.
Format: Gängiges Format, 4C (Sonderfarben & Stanzformate können gerne vorgeschlagen werden),
Versand: Print (ca. 200 Stück) & Mail
Mögliche Motive: zB 3D-Formen, grobe Pixel, etc.
Nach Rücksprache kann der Designer auch in die Veranstaltung eingearbeitet werden oder sich vor Ort den Gründern und Wirtschaftsentscheidern präsentieren.

```html
<!DOCTYPE html>
<html lang="de">
<head>
<meta charset="utf-8">
<title>#ThinkAheadNow – Einladung</title>
<link href="https://fonts.googleapis.com/css2?family=Exo+2:wght@300;400;500&display=swap" rel="stylesheet">
<style>
  :root {
    --stage: #3a3a3a;
    --card-dark: #1c1c1c;
    --card-dark-glow: #4a4a4a;
    --paper: #ffffff;
    --paper-shade: #f1f1f1;
    --ink: #2b2b2b;
    --ink-soft: #6b6b6b;
    --red: #c0272d;
    --red-bright: #e0343b;
    --line: #c9c9c9;
  }
  * { box-sizing: border-box; margin: 0; padding: 0; }
  html, body {
    width: 1200px; height: 800px; overflow: hidden;
    background: var(--stage);
    font-family: "Exo 2", Arial, sans-serif;
  }
  .canvas { position: relative; width: 1200px; height: 800px; }

  /* inside spread */
  .spread {
    position: absolute; left: 370px; top: 30px;
    width: 460px; height: 430px;
    box-shadow: 0 10px 30px rgba(0,0,0,.45);
  }
  .panel { position: relative; height: 215px; overflow: hidden; }
  .panel--greeting { background: var(--paper-shade); }
  .panel--invite { background: var(--paper); border-top: 1px solid #e2e2e2; }
  .grid-motif {
    position: absolute; inset: 0;
    background: radial-gradient(ellipse at 90% 0%, rgba(180,180,180,.35), transparent 55%),
                radial-gradient(ellipse at 10% 100%, rgba(180,180,180,.3), transparent 55%);
  }
  .panel--invite .grid-motif {
    background: radial-gradient(ellipse at 80% 100%, rgba(190,190,190,.3), transparent 60%);
  }
  .claim {
    position: absolute; color: var(--red);
    font-weight: 300; font-size: 17px; line-height: 1.05; letter-spacing: .5px;
  }
  .claim--top { left: 20px; top: 18px; }
  .claim--bottom { right: 20px; bottom: 12px; text-align: left; }
  .greeting-text {
    position: absolute; left: 20px; top: 86px; width: 420px;
    font-size: 7.4px; line-height: 1.5; color: var(--ink-soft);
  }
  .greeting-text p + p { margin-top: 6px; }
  .greeting-text em { font-style: normal; color: var(--red); }

  .invite-title {
    position: absolute; left: 22px; top: 26px;
    font-size: 11px; letter-spacing: 1.5px; color: var(--ink); font-weight: 400;
  }
  .name-line {
    position: absolute; left: 22px; right: 22px; top: 66px;
    border-bottom: 1px dashed var(--line);
  }
  .invite-line {
    position: absolute; right: 22px; top: 74px;
    font-size: 7px; color: var(--ink-soft);
  }
  .details {
    position: absolute; left: 22px; top: 112px;
    font-size: 7px; line-height: 1.55; color: var(--ink);
    display: grid; grid-template-columns: 40px auto;
  }
  .details dt { color: var(--red); }
  .rsvp {
    position: absolute; right: 22px; bottom: 24px;
    font-size: 6px; color: var(--ink-soft);
  }

  /* cover & back */
  .card {
    position: absolute; top: 495px; width: 440px; height: 265px;
    background: radial-gradient(ellipse at 50% 18%, var(--card-dark-glow), var(--card-dark) 70%);
    box-shadow: 0 10px 28px rgba(0,0,0,.5);
    overflow: hidden;
  }
  .card--cover { left: 110px; }
  .card--back { left: 650px; }
  .dome {
    position: absolute; left: 50%; top: 0; transform: translateX(-50%);
    width: 110px; height: 42px; border-radius: 0 0 55px 55px / 0 0 42px 42px;
  }
  .card--cover .dome { background: radial-gradient(ellipse at 50% 0%, rgba(224,52,59,.75), rgba(192,39,45,.2) 80%); }
  .card--back .dome { background: radial-gradient(ellipse at 50% 0%, rgba(243,243,243,.8), rgba(230,120,125,.2) 80%); }
  .event-name {
    position: absolute; left: 0; right: 0; top: 108px; text-align: center;
    color: var(--red); font-weight: 500; font-size: 32px; letter-spacing: .3px;
  }
  .sponsors { position: absolute; left: 30px; right: 30px; bottom: 28px; }
  .sponsors-label { font-size: 8px; letter-spacing: 1px; color: var(--red); margin-bottom: 12px; }
  .sponsor-list { display: flex; align-items: center; gap: 34px; list-style: none; }
  .sponsor { display: flex; align-items: center; gap: 6px; font-size: 14px; font-weight: 400; color: #ffffff; }
  .sponsor-mark { width: 12px; height: 12px; background: var(--red); }
  .sponsor-mark--round { border-radius: 50%; background: #9a9a9a; }
  .sponsor-mark--blue { background: #3c66c4; }
</style>
</head>
<body>
<main class="canvas">

  <section class="spread" aria-label="Innenseiten">
    <article class="panel panel--greeting">
      <div class="grid-motif" role="img" aria-label="Feines Gitternetz als räumliche Linienstruktur"></div>
      <h2 class="claim claim--top">YOUNG.<br>CREATIVE.<br>NIGHT.</h2>
      <div class="greeting-text">
        <p>Das Internet hat die Welt verändert und sich tief in unserer Gesellschaft verankert.<br>
        Es ist die Chance unserer Generation diese Digitalisierung zu nutzen und die Welt von morgen weiterzuentwickeln.</p>
        <p>Freuen Sie sich auf eine inspirierende Nacht im Zeichen der <em>„young leading minds of our time“</em>.<br>
        Ein Podium für Macher von heute und morgen.</p>
      </div>
      <p class="claim claim--bottom">FAST.<br>FORWARD.<br>FUTURE.</p>
    </article>

    <article class="panel panel--invite">
      <div class="grid-motif" role="img" aria-label="Feines Gitternetz als räumliche Linienstruktur"></div>
      <h2 class="invite-title">WIR FREUEN UNS</h2>
      <div class="name-line"></div>
      <p class="invite-line">zur exklusiven #ThinkAheadNow-Night einladen zu dürfen.</p>
      <dl class="details">
        <dt>Datum:</dt><dd>01. Februar 2015</dd>
        <dt>Uhrzeit:</dt><dd>ab 20:30 Uhr</dd>
        <dt>Ort:</dt><dd>xxxxxx,<br>Anfahrt über xxxxxxx</dd>
      </dl>
      <p class="rsvp">r.s.v.p. bis zum 14. Januar 2015 unter xxxxxxx</p>
    </article>
  </section>

  <section class="card card--cover" aria-label="Deckblatt">
    <div class="dome" role="img" aria-label="Rote geodätische Kuppel aus Linien"></div>
    <h1 class="event-name">#ThinkAheadNow</h1>
  </section>

  <section class="card card--back" aria-label="Rückseite">
    <div class="dome" role="img" aria-label="Helle geodätische Kuppel aus Linien"></div>
    <div class="sponsors">
      <p class="sponsors-label">SPONSOREN</p>
      <ul class="sponsor-list">
        <li class="sponsor"><span class="sponsor-mark sponsor-mark--round"></span>Vemko</li>
        <li class="sponsor"><span class="sponsor-mark"></span>Nordlicht Systems</li>
        <li class="sponsor"><span class="sponsor-mark sponsor-mark--blue"></span>Kelvar</li>
      </ul>
    </div>
  </section>

</main>
</body>
</html>
```